loma Terrace
Logo for a rehabilitation center and assisted living
Project: loma Terrace
loma Terrace - Health
Creative Brief
Neil T. Vasko
2715 Marlow Court Alder Falls, AZ 88014
brightvaleqp@mailzeno.com

```html
<!DOCTYPE html>
<html lang="en">
<head>
<meta charset="utf-8">
<title>loma Terrace — Business Card</title>
<link rel="stylesheet" href="https://fonts.googleapis.com/css2?family=Cinzel:wght@500;700&family=Cormorant+SC:wght@600&family=Arimo:wght@400&display=swap">
<style>
  :root {
    --backdrop: #8aa448;
    --card: #ffffff;
    --brand-green: #4f8c2a;
    --ink: #1d1d1b;
    --rule: #9cc36a;
  }
  * { box-sizing: border-box; margin: 0; padding: 0; }
  html, body { width: 1200px; height: 901px; overflow: hidden; }
  body { background: var(--backdrop); position: relative; font-family: "Cinzel", serif; }

  .card {
    position: absolute;
    left: 262px;
    width: 678px;
    background: var(--card);
    border-radius: 26px;
    box-shadow: 0 6px 18px rgba(0,0,0,0.25);
  }
  .card--front { top: 24px; height: 408px; }
  .card--back  { top: 466px; height: 414px; }

  .brand {
    position: absolute;
    display: flex;
    flex-direction: column;
    align-items: center;
    color: var(--brand-green);
    font-family: "Cinzel", serif;
    font-weight: 700;
  }
  .brand__mark {
    border-radius: 50%;
    background: var(--brand-green);
  }
  .card--front .brand { left: 0; right: 0; top: 90px; gap: 40px; }
  .card--front .brand__mark { width: 120px; height: 120px; }
  .card--front .brand__name { font-size: 64px; letter-spacing: 1px; }

  .card--back .brand { left: 22px; top: 22px; width: 300px; gap: 16px; }
  .card--back .brand__mark { width: 56px; height: 56px; }
  .card--back .brand__name { font-size: 30px; letter-spacing: 0.5px; }

  .holder {
    position: absolute;
    left: 0; right: 0; top: 190px;
    text-align: center;
  }
  .holder__name {
    font-family: "Cinzel", serif;
    font-weight: 700;
    font-size: 48px;
    letter-spacing: 3px;
    color: var(--brand-green);
  }
  .holder__rule {
    width: 300px; height: 2px; margin: 6px auto 8px;
    background: var(--rule);
  }
  .holder__title {
    font-family: "Cinzel", serif;
    font-weight: 500;
    font-size: 40px;
    letter-spacing: 4px;
    color: var(--ink);
  }

  .contact-email {
    position: absolute;
    left: 20px; bottom: 26px;
    display: flex; align-items: center; gap: 10px;
    font-family: "Arimo", sans-serif;
    font-size: 23px;
    color: var(--ink);
  }
  .contact-email svg { width: 30px; height: 26px; }

  .contact-address {
    position: absolute;
    right: 24px; bottom: 22px;
    text-align: right;
    font-family: "Cormorant SC", serif;
    font-style: normal;
    font-weight: 600;
    font-size: 24px;
    line-height: 1.3;
    color: var(--ink);
  }
</style>
</head>
<body>
  <section class="card card--front">
    <div class="brand">
      <span class="brand__mark"></span>
      <span class="brand__name">loma Terrace</span>
    </div>
  </section>

  <section class="card card--back">
    <div class="brand">
      <span class="brand__mark"></span>
      <span class="brand__name">loma Terrace</span>
    </div>

    <div class="holder">
      <p class="holder__name">Neil T. Vasko</p>
      <div class="holder__rule"></div>
      <p class="holder__title">Owner</p>
    </div>

    <p class="contact-email">
      <svg viewBox="0 0 30 26" aria-hidden="true">
        <rect x="1" y="4" width="28" height="20" rx="2" fill="#6aa83a"/>
        <path d="M1 6 L15 16 L29 6" fill="none" stroke="#ffffff" stroke-width="2"/>
      </svg>
      brightvaleqp@mailzeno.com
    </p>

    <address class="contact-address">
      2715 Marlow Court<br>
      Alder Falls, AZ 88014
    </address>
  </section>
</body>
</html>
```